Im looking for a sleek and sexy business card, that resembles elite or VIP status status.
our business is marnivoss.com
you can view our products on there, but our main audience for handing out our cards will be for people in the hospitality industry, so it will need to impress high management and CEO of hotels and restaurants, bars, clubs etc...
the card features will have UV spot on both sides, 400gsm stock. standard size.
Artwork should be 86 x 54mm + 2mm bleed = 90 x 58mm
it should have a nice "unique" uv spot pattern that highlights the card, not a repeated pattern, theres no originality there, and it will be disregarded.
The written material will be:
Marni Voss Hospitality College (logo)
Dena Whitby
Director
Phone: 1300 561 437
Mobile: 0439 817 265
Email: info@marnivoss.com
website: www.marnivoss.com
I'm looking for originality here, i don't want just a simple stock card, want something that has a wow factor for people.
You will find the logo attached. you may invert the white to black words to suit the background as you please.
thank you and good luck
As a side note, ive received a lot of proposals, im too busy to give feedback to each and every one, so if i havent provided feedback for your design within 24 hours, then consider it not acceptable, and you could resubmit another design.
So far i have not seen any design that stood out for me, they all seem pretty generic. there nothing thats unique, i would figure for the amount that im offering, that people would put some more effort and creativity into the design.
so far over 200 designs submitted, and nothing i have seen looks very original, everything looks like a different variation of the same stuff, i said it very clearly i wanted something unique, the only thing that has come close to it so far is this one
Reason: Ive received alot of design concepts and i have reviewed everyone, but i havent had time to give feedback to every single one, only the ones that have interested me, if i havent responded, its because i havent found it good enough.
so far only a few design have been on par with what ive been looking for, an attractive eye popping design.
heres a few of them,
http://files.pitchgallery.net/design_img/51846/62937/62937_2846105_51846_image.jpg
http://files.pitchgallery.net/design_img/51846/58714/58714_2846592_51846_image.jpg
theyre, both unique and original, and eye catching, the only thing theyre missing is the sexyness.
if you still think you have some creativity left in your minds, then throw it on here.
Reason: Sorry guys for the delay, I was in a serious accident and out of commission for the past few months, I'm just slowly recovering now, please bare with me as i try to attend to this project, it may take me awhile as I have other projects that are on standby, I'm not 100% at the moment, so im extending the deadline for 2 weeks right now. Thanks for your patience.

```html
<!DOCTYPE html>
<html lang="en">
<head>
<meta charset="utf-8">
<title>Marni Voss Hospitality College – Business Card</title>
<link href="https://fonts.googleapis.com/css2?family=Barlow+Semi+Condensed:wght@500;600;700&display=swap" rel="stylesheet">
<style>
  :root {
    --bg: #e6e4e1;
    --card-blue: #4ba3d4;
    --card-dark: #29292b;
    --accent-blue: #55b0df;
    --white: #ffffff;
    --shadow: rgba(0, 0, 0, 0.28);
  }
  * { box-sizing: border-box; margin: 0; padding: 0; }
  html, body {
    width: 1200px;
    height: 1000px;
    overflow: hidden;
    background: var(--bg);
    font-family: "Barlow Semi Condensed", "Arial Narrow", sans-serif;
  }
  .sheet {
    width: 1200px;
    height: 1000px;
    display: flex;
    flex-direction: column;
    align-items: center;
    justify-content: center;
    gap: 44px;
  }
  .card {
    position: relative;
    width: 700px;
    height: 440px;
    border-radius: 4px;
    box-shadow: 0 14px 30px var(--shadow);
    overflow: hidden;
  }

  /* Back: contact side */
  .card--contact {
    background: var(--card-blue);
    color: var(--white);
    text-align: center;
  }
  .brand {
    position: absolute;
    top: 30px;
    left: 0;
    right: 0;
    display: flex;
    justify-content: center;
    align-items: center;
    gap: 10px;
    font-weight: 600;
    font-size: 17px;
    letter-spacing: 0.06em;
    text-transform: uppercase;
    color: var(--white);
  }
  .brand__mark {
    width: 22px;
    height: 22px;
    background: var(--white);
  }
  .person {
    position: absolute;
    top: 132px;
    left: 0;
    right: 0;
  }
  .person__name {
    font-weight: 700;
    font-size: 50px;
    letter-spacing: 0.03em;
    text-transform: uppercase;
    line-height: 1;
  }
  .person__role {
    margin-top: 6px;
    font-weight: 700;
    font-size: 20px;
    letter-spacing: 0.08em;
    text-transform: uppercase;
  }
  .contact {
    position: absolute;
    top: 262px;
    left: 0;
    right: 0;
    list-style: none;
    font-weight: 600;
    font-size: 19px;
    line-height: 1.45;
    letter-spacing: 0.04em;
  }
  .contact__label { text-transform: uppercase; }

  /* Front: brand side */
  .card--brand {
    background: var(--card-dark);
  }
  .brand-block {
    position: absolute;
    left: 60px;
    top: 60px;
    width: 320px;
    height: 320px;
    background: var(--accent-blue);
  }
  .brand-name {
    position: absolute;
    left: 410px;
    top: 0;
    bottom: 0;
    display: flex;
    flex-direction: column;
    justify-content: center;
    font-weight: 600;
    color: var(--white);
    text-transform: uppercase;
    line-height: 1;
  }
  .brand-name__line--main {
    font-size: 60px;
    letter-spacing: 0.02em;
  }
  .brand-name__line--sub {
    margin-top: 10px;
    font-size: 27px;
    letter-spacing: 0.04em;
  }
</style>
</head>
<body>
  <main class="sheet">
    <section class="card card--contact" aria-label="Business card, contact side">
      <div class="brand">
        <span class="brand__mark" aria-hidden="true"></span>
        <span class="brand__name">Marni Voss Hospitality College</span>
      </div>
      <div class="person">
        <h1 class="person__name">Dena Whitby</h1>
        <p class="person__role">Director</p>
      </div>
      <ul class="contact">
        <li><span class="contact__label">Phone:</span> 1300 561 437</li>
        <li><span class="contact__label">Mobile:</span> 0439 817 265</li>
        <li><span class="contact__label">Email:</span> info@marnivoss.com</li>
        <li><span class="contact__label">Web:</span> www.marnivoss.com</li>
      </ul>
    </section>

    <section class="card card--brand" aria-label="Business card, brand side">
      <div class="brand-block" aria-hidden="true"></div>
      <div class="brand-name">
        <span class="brand-name__line brand-name__line--main">Marni Voss</span>
        <span class="brand-name__line brand-name__line--sub">Hospitality College</span>
      </div>
    </section>
  </main>
</body>
</html>
```